Keystone Haulers Billboard design

I need two billboard designs using our logo and adding a few words Looking for a black background with our logo and wording in either purple or white.

need it to have our website keystonehaulers-example.com. phone number 555 201 4387

Also have 16/20/30 yard dumpsters available!

one billboard is size 7x21 feet the other is 15x 21 ft

Target Market(s)

Contractors, home owners

Requirements
Must have
• Use font similar to logo that is eye catching

```html
<!DOCTYPE html>
<html lang="en">
<head>
<meta charset="utf-8">
<title>Keystone Haulers Billboards</title>
<link href="https://fonts.googleapis.com/css2?family=Exo+2:wght@500;600;700;800&display=swap" rel="stylesheet">
<style>
  :root {
    --page: #f9f9f9;
    --purple: #7b3d98;
    --purple-deep: #3a1a4a;
    --ink: #150a18;
    --white: #ffffff;
    --edge: #dcdcdc;
  }
  * { margin: 0; padding: 0; box-sizing: border-box; }
  html, body { width: 1081px; height: 1200px; overflow: hidden; background: var(--page); }
  body { position: relative; font-family: "Exo 2", sans-serif; color: var(--white); }

  .billboard { position: absolute; overflow: hidden; background: var(--white); border: 1px solid var(--edge); }
  .billboard--wide { left: 115px; top: 127px; width: 851px; height: 283px; }
  .billboard--tall { left: 124px; top: 468px; width: 851px; height: 608px; }

  .photo { position: absolute; inset: 0; }
  .billboard--wide .photo { background: linear-gradient(100deg, var(--purple) 0%, #5b2c70 30%, var(--purple-deep) 48%, var(--ink) 70%, #24102c 100%); }
  .billboard--tall .photo { background: linear-gradient(110deg, var(--purple) 0%, #5b2c70 35%, var(--purple-deep) 55%, var(--ink) 75%, #2a1234 100%); }

  .tear { position: absolute; left: 0; width: 100%; }
  .abs { position: absolute; }

  .brand { font-weight: 700; text-transform: uppercase; color: var(--white); line-height: 0.95; letter-spacing: 1px; white-space: nowrap; }
  .headline { font-weight: 600; text-transform: uppercase; line-height: 1; letter-spacing: 0.5px; white-space: nowrap; }

  .sizes { display: flex; align-items: flex-end; }
  .size { display: flex; flex-direction: column; align-items: center; font-weight: 800; line-height: 0.9; }
  .size__yard { font-weight: 700; }
  .size-divider { background: var(--white); transform: skewX(-18deg); opacity: 0.9; }

  .cta-lead { font-weight: 600; text-transform: uppercase; text-align: center; white-space: nowrap; }
  .cta-button { border: 2px solid var(--white); border-radius: 40px; display: flex; align-items: center; justify-content: center; font-weight: 600; text-transform: uppercase; white-space: nowrap; }

  .contact { position: absolute; display: flex; align-items: center; color: var(--purple); white-space: nowrap; line-height: 1; transform: translateY(-50%); }
  .contact__phone { font-weight: 600; letter-spacing: 1px; }
  .contact__web { font-weight: 600; text-transform: uppercase; }
</style>
</head>
<body>

<!-- 7 x 21 ft billboard -->
<section class="billboard billboard--wide">
  <div class="photo" role="img" aria-label="Roll-off truck unloading a dumpster, tinted purple and black"></div>
  <svg class="tear" style="top:150px;height:133px" viewBox="0 0 851 133" preserveAspectRatio="none">
    <path d="M0 14 C60 6 120 22 180 16 C240 10 290 30 350 40 C410 50 470 70 540 60 C590 54 620 40 660 44 C700 48 730 58 760 30 C790 10 820 24 851 18 L851 133 L0 133 Z" fill="#e4e4e4"/>
    <path d="M0 34 C70 28 130 40 190 36 C260 32 320 52 380 60 C440 68 500 84 560 74 C610 66 650 56 690 62 C730 68 770 72 800 52 C825 38 840 42 851 40 L851 133 L0 133 Z" fill="var(--white)"/>
  </svg>

  <div class="abs brand" style="left:49px;top:42px;font-size:34px;">Keystone<br><span style="font-size:26px;padding-left:40px;">Haulers</span></div>

  <h2 class="abs headline" style="left:335px;top:43px;font-size:31px;">Residential &amp; Commercial<br>Dumpster Rentals</h2>

  <div class="abs sizes" style="left:328px;top:122px;gap:10px;">
    <div class="size"><span style="font-size:46px;">16</span><span class="size__yard" style="font-size:21px;">yard</span></div>
    <div class="size-divider" style="width:1.5px;height:56px;"></div>
    <div class="size"><span style="font-size:46px;">20</span><span class="size__yard" style="font-size:21px;">yard</span></div>
    <div class="size-divider" style="width:1.5px;height:56px;"></div>
    <div class="size"><span style="font-size:46px;">30</span><span class="size__yard" style="font-size:21px;">yard</span></div>
  </div>

  <p class="abs cta-lead" style="left:600px;top:127px;width:224px;font-size:12px;">Rent your dumpster today</p>
  <div class="abs cta-button" style="left:600px;top:148px;width:224px;height:36px;font-size:21px;padding-left:24px;">Book now at</div>

  <svg class="abs" style="left:752px;top:194px;" width="46" height="60" viewBox="0 0 46 60">
    <path d="M30 2 C42 22 36 42 10 48" fill="none" stroke="var(--purple)" stroke-width="3"/>
    <path d="M2 49 L14 40 L13 56 Z" fill="var(--purple)"/>
  </svg>

  <div class="contact" style="left:47px;top:245px;">
    <svg width="32" height="32" viewBox="0 0 32 32"><circle cx="16" cy="16" r="16" fill="var(--purple)"/><path d="M11 8 L14 12 L12.5 14 C13.5 16.5 15.5 18.5 18 19.5 L20 18 L24 21 L22 24 C15 24 8 17 8 10 Z" fill="var(--white)"/></svg>
    <span class="contact__phone" style="font-size:40px;margin-left:12px;">555 201 4387</span>
  </div>
  <div class="contact" style="left:381px;top:245px;">
    <svg width="26" height="26" viewBox="0 0 26 26"><circle cx="13" cy="13" r="13" fill="var(--purple)"/><g fill="none" stroke="var(--white)" stroke-width="1.2"><circle cx="13" cy="13" r="7.5"/><ellipse cx="13" cy="13" rx="3.5" ry="7.5"/><path d="M5.5 13 H20.5 M7 9 H19 M7 17 H19"/></g></svg>
    <span class="contact__web" style="font-size:19px;margin-left:10px;">keystonehaulers-example.com</span>
  </div>
</section>

<!-- 15 x 21 ft billboard -->
<section class="billboard billboard--tall">
  <div class="photo" role="img" aria-label="Roll-off truck unloading a dumpster, tinted purple and black"></div>
  <svg class="tear" style="top:345px;height:263px" viewBox="0 0 851 263" preserveAspectRatio="none">
    <path d="M0 10 C60 0 110 20 170 30 C230 40 260 60 320 70 C380 80 420 100 470 110 C520 120 560 90 600 110 C640 130 690 100 730 80 C770 60 810 40 851 20 L851 263 L0 263 Z" fill="#e2e2e2"/>
    <path d="M0 60 C60 55 120 70 180 78 C240 86 290 100 340 118 C400 140 450 150 500 140 C550 130 580 120 620 128 C660 136 700 150 740 130 C780 110 820 100 851 96 L851 263 L0 263 Z" fill="var(--white)"/>
  </svg>

  <h1 class="abs headline" style="left:42px;top:49px;font-size:62px;line-height:54px;">Residential &amp;<br>Commercial<br>Dumpster<br>Rentals</h1>

  <div class="abs brand" style="left:578px;top:42px;font-size:40px;">Keystone<br><span style="font-size:31px;padding-left:50px;">Haulers</span></div>

  <div class="abs sizes" style="left:494px;top:218px;gap:16px;">
    <div class="size"><span style="font-size:62px;">16</span><span class="size__yard" style="font-size:32px;">yard</span></div>
    <div class="size-divider" style="width:1.5px;height:80px;"></div>
    <div class="size"><span style="font-size:62px;">20</span><span class="size__yard" style="font-size:32px;">yard</span></div>
    <div class="size-divider" style="width:1.5px;height:80px;"></div>
    <div class="size"><span style="font-size:62px;">30</span><span class="size__yard" style="font-size:32px;">yard</span></div>
  </div>

  <p class="abs cta-lead" style="left:502px;top:343px;width:313px;font-size:17px;">Rent your dumpster today</p>
  <div class="abs cta-button" style="left:502px;top:372px;width:313px;height:49px;font-size:29px;padding-left:40px;">Book now at</div>

  <svg class="abs" style="left:650px;top:434px;" width="48" height="78" viewBox="0 0 48 78">
    <path d="M4 2 C40 14 44 48 14 66" fill="none" stroke="var(--purple)" stroke-width="3.5"/>
    <path d="M2 74 L10 58 L20 70 Z" fill="var(--purple)"/>
  </svg>

  <div class="contact" style="left:47px;top:554px;">
    <svg width="36" height="36" viewBox="0 0 32 32"><circle cx="16" cy="16" r="16" fill="var(--purple)"/><path d="M11 8 L14 12 L12.5 14 C13.5 16.5 15.5 18.5 18 19.5 L20 18 L24 21 L22 24 C15 24 8 17 8 10 Z" fill="var(--white)"/></svg>
    <span class="contact__phone" style="font-size:46px;margin-left:12px;">555 201 4387</span>
  </div>
  <div class="contact" style="left:415px;top:554px;">
    <svg width="30" height="30" viewBox="0 0 26 26"><circle cx="13" cy="13" r="13" fill="var(--purple)"/><g fill="none" stroke="var(--white)" stroke-width="1.2"><circle cx="13" cy="13" r="7.5"/><ellipse cx="13" cy="13" rx="3.5" ry="7.5"/><path d="M5.5 13 H20.5 M7 9 H19 M7 17 H19"/></g></svg>
    <span class="contact__web" style="font-size:21px;margin-left:10px;">keystonehaulers-example.com</span>
  </div>
</section>

</body>
</html>
```